Craft oriented film company needs a Business Card design

Hi all,
We're a 2-man band film company in New Zealand called Kestrel Pictures. We're good honest blokes, who are very passionate about the craft of film making. I've attached our current logo which has a bit of a crafty/artisan feel that we like. Feel free to use it - or throw the baby out with the bathwater and start again..... you never know, you might inspire a complete brand re-work.

In any case, the vibe we want to give out is that we are solid, dependable and no bullshit - but without compromising creative excellence and being in the now. We like the 'Brooklyn' artisan style of work.

Preferably single sided.

We need the standard stuff:
Name, job title, cellphone, email address and physical address (this can be smaller if you like - street, suburb, city & zip, country [if you want])

Check out our website to learn more about us: kestrelpictures.example

Target Market(s)

Brand marketers and advertising agency creatives looking for video production.

Industry/Entity Type

Baby

Requirements
Should not have
• Nothing flashy or too 'futuristic', we want it to feel grounded and real. A limited colour palette is preferred.
We don't want any film reels or cameras or anything obvious like that.

```html
<!DOCTYPE html>
<html lang="en">
<head>
<meta charset="utf-8">
<title>Kestrel Pictures – Business Card</title>
<link rel="stylesheet" href="https://fonts.googleapis.com/css2?family=Ubuntu:wght@400;700&display=swap">
<style>
  :root {
    --backdrop: #2b2b2b;
    --card-light: #ececec;
    --card-mid: #dcdcdc;
    --ink: #2a2a2a;
    --ink-soft: #6a6a6a;
    --band: #1c1c1c;
    --badge: #111111;
    --badge-ring: #f4f4f4;
    --accent: #3a9bd5;
    --white: #ffffff;
  }
  * { box-sizing: border-box; margin: 0; padding: 0; }
  html, body {
    width: 1200px; height: 1000px; overflow: hidden;
    background: var(--backdrop);
    font-family: "Ubuntu", sans-serif;
  }
  .business-card {
    position: absolute; left: 150px; top: 243px;
    width: 900px; height: 514px;
    background: linear-gradient(135deg, var(--card-mid) 0%, var(--card-light) 55%, var(--card-mid) 100%);
    overflow: hidden;
  }
  .card-band { position: absolute; left: 0; bottom: 0; width: 900px; height: 130px; }
  .identity { position: absolute; left: 96px; top: 180px; }
  .person-name { font-size: 30px; font-weight: 700; color: var(--ink); letter-spacing: 0.5px; }
  .person-role { font-size: 16px; color: var(--ink-soft); margin-top: 6px; margin-left: 6px; }
  .contact-list { position: absolute; left: 96px; top: 296px; list-style: none; }
  .contact-item {
    display: flex; align-items: flex-start; gap: 16px;
    font-size: 18px; color: var(--ink-soft); line-height: 22px; margin-bottom: 18px;
  }
  .contact-icon { flex: 0 0 22px; width: 22px; height: 22px; margin-top: 1px; }
  .brand-badge {
    position: absolute; left: 632px; top: 196px;
    width: 220px; height: 220px; border-radius: 50%;
    background: var(--badge);
    border: 8px solid var(--badge-ring);
    display: flex; align-items: center; justify-content: center; text-align: center;
  }
  .brand-name {
    font-size: 27px; font-weight: 700; color: var(--white);
    line-height: 32px; letter-spacing: 1px;
  }
</style>
</head>
<body>
  <div class="business-card">
    <svg class="card-band" viewBox="0 0 900 130" aria-hidden="true">
      <polygon points="0,78 560,78 620,0 900,0 900,130 0,130" fill="var(--band)"/>
    </svg>

    <div class="identity">
      <h1 class="person-name">PERSON NAME</h1>
      <p class="person-role">Designation</p>
    </div>

    <ul class="contact-list">
      <li class="contact-item">
        <svg class="contact-icon" viewBox="0 0 22 22" aria-hidden="true">
          <circle cx="11" cy="11" r="11" fill="var(--accent)"/>
          <path d="M7.5 6.5c.6-.6 1.4-.5 1.8.1l.9 1.4c.3.5.2 1-.2 1.4l-.6.5c.5 1.1 1.3 2 2.4 2.5l.5-.6c.4-.4 1-.5 1.4-.2l1.4.9c.6.4.7 1.2.1 1.8-1 1-2.7 1.1-4.4-.2-1.4-1-2.6-2.3-3.4-3.8-.8-1.5-.6-3 .1-3.8z" fill="var(--white)"/>
        </svg>
        <span>000-555-0187</span>
      </li>
      <li class="contact-item">
        <svg class="contact-icon" viewBox="0 0 22 22" aria-hidden="true">
          <circle cx="11" cy="11" r="11" fill="var(--accent)"/>
          <path d="M11 6l5 4.5h-1.5V15h-2.5v-3h-2v3H7.5v-4.5H6z" fill="var(--white)"/>
        </svg>
        <span>Your street address<br>will be here</span>
      </li>
      <li class="contact-item">
        <svg class="contact-icon" viewBox="0 0 22 22" aria-hidden="true">
          <circle cx="11" cy="11" r="11" fill="var(--accent)"/>
          <rect x="6" y="7.5" width="10" height="7" rx="1" fill="var(--white)"/>
          <path d="M6.5 8l4.5 3.5L15.5 8" stroke="var(--accent)" stroke-width="1" fill="none"/>
        </svg>
        <span>mailid@kestrelpictures.example</span>
      </li>
    </ul>

    <div class="brand-badge">
      <p class="brand-name">KESTREL<br>PICTURES</p>
    </div>
  </div>
</body>
</html>
```